Modern Lawfirm Business Card Design

We're looking for a business card to incorporate the newly created logo we had made.

Ideally looking for a law firm business card demonstrating, modern, minimalist, strong/bold design.

I'm open to any design honestly, but nothing "flashy".

Target Market(s)

Immigration law, family immigration, humanitarian, general legal

Industry/Entity Type

Law Firm

Contact Information for Business Card

Please use dummy information, name, street address, city, state, phone number, email, website.

Font styles to use
Serif
Sans Serif

Requirements
Must have
• Please use dummy information, name, street address, city, state, phone number, email, website.

```html
<!DOCTYPE html>
<html lang="en">
<head>
<meta charset="utf-8">
<title>Halvern Immigration Law – Business Card</title>
<link rel="stylesheet" href="https://fonts.googleapis.com/css2?family=Lato:wght@400;700;900&display=swap">
<style>
  :root {
    --brand-blue: #3e5c98;
    --card-white: #ffffff;
    --ink: #1c1c1c;
    --accent-grey: #9a9a9a;
    --stage: #2b2b2b;
  }
  * { margin: 0; padding: 0; box-sizing: border-box; }
  html, body { width: 1200px; height: 1166px; overflow: hidden; }
  body {
    background: var(--stage);
    font-family: "Lato", Arial, sans-serif;
    position: relative;
  }
  .card {
    position: absolute;
    left: 220px;
    width: 760px;
    height: 434px;
    overflow: hidden;
  }
  .card--back { top: 100px; background: var(--brand-blue); }
  .card--front { top: 620px; background: var(--card-white); }

  .wordmark {
    display: flex;
    align-items: center;
    gap: 14px;
    color: var(--card-white);
    font-weight: 900;
  }
  .wordmark__square {
    width: 22px; height: 22px;
    background: currentColor;
    flex: none;
  }
  .wordmark__name { font-size: 50px; letter-spacing: 2px; line-height: 1; }
  .wordmark__sub {
    display: block;
    font-size: 15px;
    letter-spacing: 9px;
    margin-top: 8px;
  }

  .card--back .wordmark {
    position: absolute;
    left: 0; right: 0; top: 150px;
    justify-content: center;
  }
  .card--back .website {
    position: absolute;
    left: 0; right: 0; top: 330px;
    text-align: center;
    color: var(--card-white);
    font-size: 17px;
    letter-spacing: 4px;
  }

  .card--front .wordmark {
    position: absolute;
    left: 52px; top: 48px;
    color: var(--brand-blue);
  }
  .card--front .wordmark__name { font-size: 40px; }
  .card--front .wordmark__sub { font-size: 12px; letter-spacing: 7px; }

  .holder { position: absolute; left: 92px; top: 168px; }
  .holder__name { color: var(--brand-blue); font-weight: 900; font-size: 32px; line-height: 1.1; }
  .holder__role { color: var(--ink); font-size: 19px; margin-top: 2px; }

  .contacts {
    position: absolute;
    left: 92px; top: 250px;
    list-style: none;
  }
  .contacts li {
    display: flex; align-items: center; gap: 16px;
    font-size: 20px; color: var(--ink);
    height: 26px;
  }
  .contacts svg { width: 18px; height: 18px; fill: var(--brand-blue); flex: none; }

  .address {
    position: absolute;
    right: 70px; top: 176px;
    font-size: 19px; color: var(--ink); line-height: 1.3;
  }
  .stripes { position: absolute; inset: 0; }
</style>
</head>
<body>

<section class="card card--back" aria-label="Card back">
  <div class="wordmark">
    <span class="wordmark__square"></span>
    <div>
      <span class="wordmark__name">HALVERN</span>
      <span class="wordmark__sub">IMMIGRATION LAW</span>
    </div>
  </div>
  <p class="website">www.halvernlaw.com</p>
</section>

<section class="card card--front" aria-label="Card front">
  <svg class="stripes" viewBox="0 0 760 434" aria-hidden="true">
    <polygon points="300,360 735,360 720,382 285,382" fill="var(--brand-blue)"/>
    <polygon points="0,404 185,404 198,434 0,434" fill="var(--brand-blue)"/>
    <polygon points="212,386 262,386 250,414 200,414" fill="var(--accent-grey)"/>
  </svg>

  <div class="wordmark">
    <span class="wordmark__square"></span>
    <div>
      <span class="wordmark__name">HALVERN</span>
      <span class="wordmark__sub">IMMIGRATION LAW</span>
    </div>
  </div>

  <div class="holder">
    <p class="holder__name">Daniel Ruiz</p>
    <p class="holder__role">Manager</p>
  </div>

  <ul class="contacts">
    <li><svg viewBox="0 0 24 24"><path d="M6.6 10.8a15 15 0 0 0 6.6 6.6l2.2-2.2a1 1 0 0 1 1-.25 11.4 11.4 0 0 0 3.6.57 1 1 0 0 1 1 1V20a1 1 0 0 1-1 1A17 17 0 0 1 3 4a1 1 0 0 1 1-1h3.5a1 1 0 0 1 1 1c0 1.25.2 2.45.57 3.57a1 1 0 0 1-.25 1z"/></svg>555 014 2200</li>
    <li><svg viewBox="0 0 24 24"><path d="M6 3h12v5H6zM4 9h16a2 2 0 0 1 2 2v6h-4v4H6v-4H2v-6a2 2 0 0 1 2-2zm4 7v3h8v-3z"/></svg>555 014 2201</li>
    <li><svg viewBox="0 0 24 24"><path d="M2 5h20v14H2zm2 2v.5l8 5 8-5V7l-8 5z"/></svg>info@halvernlaw.com</li>
    <li><svg viewBox="0 0 24 24"><path d="M12 2a10 10 0 1 0 0 20 10 10 0 0 0 0-20zm6.9 9h-3a15 15 0 0 0-1.3-5.6A8 8 0 0 1 18.9 11zM12 4c.9 1.3 1.7 3.8 1.9 7h-3.8C10.3 7.8 11.1 5.3 12 4zM9.4 5.4A15 15 0 0 0 8.1 11h-3a8 8 0 0 1 4.3-5.6zM5.1 13h3a15 15 0 0 0 1.3 5.6A8 8 0 0 1 5.1 13zM12 20c-.9-1.3-1.7-3.8-1.9-7h3.8c-.2 3.2-1 5.7-1.9 7zm2.6-1.4a15 15 0 0 0 1.3-5.6h3a8 8 0 0 1-4.3 5.6z"/></svg>www.halvernlaw.com</li>
  </ul>

  <address class="address" style="font-style: normal;">
    1480 Elm Ridge Ave<br>Lakeview TX 75000
  </address>
</section>

</body>
</html>
```